Homebrew-webshop picture design

I need help with catogory-pics and frontpage-pics for my homebrew-webshop: http://maltkisten.test47.webfjordhost.dk/

My main buiness is raw materials and equipment for small scale beer-brewing.
I would like the pics is welcoming and descriptive.
Cues: Quality products, Customer Care, Personal service,

```html
<!DOCTYPE html>
<html lang="en">
<head>
<meta charset="utf-8">
<title>Maltkisten.dk – Homebrew webshop</title>
<link href="https://fonts.googleapis.com/css2?family=Lato:ital,wght@0,400;0,700;0,900;1,400&display=swap" rel="stylesheet">
<style>
:root{
  --blue:#1553a9;
  --blue-dark:#0f3f82;
  --ink:#222;
  --topbar:#2e3540;
  --band:#3b4552;
  --footer:#3a4350;
  --soft:#f2f2f2;
  --line:#cfcfcf;
  --badge:#2a2a2a;
}
*{box-sizing:border-box;margin:0;padding:0}
html,body{width:1200px;height:4695px;overflow:hidden}
body{position:relative;font-family:'Lato',sans-serif;color:var(--ink);background:#fff}
.abs{position:absolute}
.topbar{left:0;top:0;width:1200px;height:49px;background:var(--topbar);color:#fff;font-size:14px;font-weight:700;display:flex;align-items:center;justify-content:center;gap:14px}
.logo{left:75px;top:90px;font-size:40px;color:var(--blue);letter-spacing:-0.5px}
.search{left:514px;top:95px;width:504px;height:42px;border:1px solid var(--line);font-size:13px;color:#777;padding:12px 16px}
.search svg{position:absolute;right:14px;top:11px}
.nav{left:0;top:177px;width:1200px;height:55px;background:var(--blue);display:flex;padding-left:75px}
.nav a{color:#fff;font-size:13px;font-weight:700;text-decoration:none;padding:0 21px;line-height:55px}
.nav a.active{background:var(--blue-dark)}
.photo{position:absolute}
.hero{left:0;top:232px;width:1200px;height:523px;background:
  radial-gradient(ellipse 260px 300px at 820px 380px,rgba(240,180,40,.95),rgba(240,180,40,0) 70%),
  radial-gradient(ellipse 300px 200px at 180px 140px,rgba(200,140,60,.8),rgba(200,140,60,0) 70%),
  radial-gradient(ellipse 400px 160px at 200px 500px,rgba(70,110,30,.9),rgba(70,110,30,0) 70%),
  radial-gradient(ellipse 300px 160px at 1050px 500px,rgba(80,120,30,.9),rgba(80,120,30,0) 70%),
  linear-gradient(90deg,#2e2418,#6a4a28 35%,#4a3826 60%,#2a2018)}
.hero-title{left:0;top:410px;width:1200px;text-align:center;color:#fff;font-size:48px;font-weight:900;text-shadow:0 2px 6px rgba(0,0,0,.4)}
.hero-sub{left:0;top:474px;width:1200px;text-align:center;color:#fff;font-size:26px;font-weight:700;text-shadow:0 2px 6px rgba(0,0,0,.4)}
.btn{display:inline-block;background:var(--blue);color:#fff;font-size:17px;font-weight:700;text-align:center}
.arrow{position:absolute}
.tile{position:absolute;display:flex;align-items:center;justify-content:center;color:#fff;font-weight:900;font-size:28px;text-align:center;text-shadow:0 2px 6px rgba(0,0,0,.45)}
.section-title{position:absolute;left:0;width:1200px;text-align:center;font-size:32px;font-weight:700}
.welcome-bg{left:587px;top:1432px;width:613px;height:425px;background:#ebebeb}
.welcome-h{left:614px;top:1488px;font-size:33px;font-weight:700}
.welcome-h span{color:var(--blue)}
.welcome-p{left:614px;top:1544px;width:520px;font-size:13.5px;line-height:27.5px;color:#333}
.prod{position:absolute;width:240px;text-align:center}
.prod .img{width:200px;height:220px;margin:0 auto}
.prod h4{font-size:16px;font-weight:700;margin-top:46px}
.prod p{font-size:14px;color:#444;margin-top:8px}
.prod s{display:block;font-size:14px;color:#777;margin-top:8px}
.prod b{display:block;font-size:17px;color:var(--blue);margin-top:6px}
.brands{left:0;top:2417px;width:1200px;height:259px;background:var(--soft)}
.badge{position:absolute;border:4px solid var(--badge)}
.mail{left:0;top:3116px;width:1200px;height:145px;background:var(--band)}
.mail-h{left:180px;top:3166px;color:#fff;font-size:32px}
.mail-in{left:518px;top:3168px;width:450px;height:40px;background:#fff;font-size:13px;color:#555;padding:12px 14px}
.mail-go{left:968px;top:3168px;width:50px;height:40px;background:var(--blue)}
.quote{left:160px;top:3378px;width:880px;text-align:center;font-size:16px;font-style:italic;line-height:29px;color:#333}
.quote-by{left:0;top:3446px;width:1200px;text-align:center;color:var(--blue);font-size:14px;font-weight:700}
.blog{left:0;top:3539px;width:1200px;height:578px;background:var(--soft)}
.blog-date{font-size:13px;color:var(--blue);font-weight:700}
.blog-title{font-size:23px;line-height:32px;width:520px}
.feature{position:absolute;top:4166px;width:331px;height:152px;border:2px solid #ddd;text-align:center;background:#fff}
.feature svg{margin-top:28px}
.feature h5{color:var(--blue);font-size:18px;font-weight:700;margin-top:10px}
.feature p{font-size:14px;margin-top:6px}
.footer{left:0;top:4363px;width:1200px;height:332px;background:var(--footer)}
.fcol{position:absolute;top:4405px;font-size:14px;line-height:32px;color:#e6e6e6}
.fcol h6{font-size:14px;font-weight:700;color:#fff;margin-bottom:6px;line-height:20px}
.fcol.contact{line-height:27px}
.social{position:absolute;top:4451px;width:24px;height:24px;border-radius:50%;background:#fff}
.fline{left:75px;top:4624px;width:1050px;height:1px;background:#5a6370}
.copy{left:75px;top:4656px;font-size:12px;color:#ccc}
.card{position:absolute;top:4652px;width:40px;height:24px;background:#e8e8ee;border-radius:3px}
</style>
</head>
<body>

<div class="abs topbar">
  <span>Shipping only DKK 35</span><span>/</span><span>Free shipping on Buy over 500</span><span>/</span><span>Secure payment 30 day return policy</span>
</div>

<div class="abs logo">Maltkisten.dk</div>
<div class="abs search">Search...
  <svg width="18" height="18" viewBox="0 0 18 18"><circle cx="7.5" cy="7.5" r="5.5" fill="none" stroke="#222" stroke-width="2.2"/><line x1="11.5" y1="11.5" x2="16" y2="16" stroke="#222" stroke-width="2.4"/></svg>
</div>
<svg class="abs" style="left:1052px;top:106px" width="18" height="18" viewBox="0 0 18 18"><circle cx="9" cy="5" r="4" fill="#222"/><path d="M1 17c0-5 4-7 8-7s8 2 8 7z" fill="#222"/></svg>
<svg class="abs" style="left:1090px;top:106px" width="20" height="18" viewBox="0 0 20 18"><path d="M0 1h4l3 10h10l2-7H6" fill="none" stroke="#222" stroke-width="2.4"/><circle cx="8" cy="15" r="2" fill="#222"/><circle cx="16" cy="15" r="2" fill="#222"/></svg>
<div class="abs" style="left:1117px;top:98px;font-size:12px;color:var(--blue);font-weight:700">0</div>

<nav class="abs nav">
  <a class="active" href="#">HOME</a><a href="#">COMMODITIES</a><a href="#">BREWING AND FERMENTATION</a><a href="#">BOTTLING</a><a href="#">CLEANING</a><a href="#">LABORATORIET</a><a href="#">SNAPS</a><a href="#">BOOKS</a>
</nav>

<div class="photo hero" role="img" aria-label="Copper brew kettles behind a frothy glass of golden beer surrounded by fresh hops"></div>
<div class="abs hero-title">WELCOME TO MALTKISTEN</div>
<div class="abs hero-sub">Neque porro quisquam est qui dolorem.</div>
<div class="abs btn" style="left:525px;top:541px;width:150px;height:50px;line-height:50px">Shop Now</div>
<svg class="arrow" style="left:93px;top:455px" width="16" height="34" viewBox="0 0 16 34"><path d="M14 2 2 17l12 15" fill="none" stroke="#fff" stroke-width="2.5"/></svg>
<svg class="arrow" style="left:1088px;top:455px" width="16" height="34" viewBox="0 0 16 34"><path d="M2 2l12 15L2 32" fill="none" stroke="#fff" stroke-width="2.5"/></svg>

<div class="tile" style="left:75px;top:786px;width:512px;height:276px;background:radial-gradient(ellipse 220px 130px at 240px 150px,#a07848,rgba(160,120,72,0) 75%),radial-gradient(ellipse 120px 80px at 420px 60px,#7a5a36,rgba(0,0,0,0) 75%),linear-gradient(135deg,#3e2e1e,#6a5034 50%,#4a3824)" role="img" aria-label="Barley malt grain in a sack with dried barley ears">COMMODITES</div>
<div class="tile" style="left:615px;top:786px;width:512px;height:276px;background:radial-gradient(ellipse 200px 140px at 380px 90px,#a0643a,rgba(160,100,58,0) 75%),radial-gradient(ellipse 160px 120px at 120px 200px,#6a3e24,rgba(0,0,0,0) 75%),linear-gradient(135deg,#2a1610,#5a3420 55%,#2e1c12)" role="img" aria-label="Copper brewing and fermentation vessels">BREWING &amp; FERMENTATION</div>
<div class="tile" style="left:75px;top:1089px;width:330px;height:275px;background:radial-gradient(ellipse 120px 100px at 170px 120px,#6a3828,rgba(106,56,40,0) 75%),linear-gradient(135deg,#1a1616,#3a2a24 55%,#222020)" role="img" aria-label="Dark brown beer bottles with caps">BOTTLING</div>
<div class="tile" style="left:436px;top:1089px;width:330px;height:275px;background:radial-gradient(ellipse 60px 130px at 100px 140px,#d4d8dc,rgba(212,216,220,0) 75%),radial-gradient(ellipse 60px 130px at 230px 140px,#d0d4d8,rgba(208,212,216,0) 75%),linear-gradient(135deg,#5a6068,#8a9098 55%,#646a72)" role="img" aria-label="Clean upside-down glass carboys">CLEANING</div>
<div class="tile" style="left:797px;top:1089px;width:330px;height:275px;background:radial-gradient(ellipse 100px 90px at 220px 220px,#f2f4f6,rgba(242,244,246,0) 75%),radial-gradient(ellipse 60px 80px at 200px 70px,#6a7a4a,rgba(0,0,0,0) 75%),linear-gradient(135deg,#7a8ca0,#b4c0cc 55%,#8a9aae)" role="img" aria-label="Gloved hands using laboratory test equipment">LABORATORIET</div>

<div class="photo" style="left:0;top:1432px;width:587px;height:425px;background:radial-gradient(ellipse 110px 70px at 390px 120px,#c8b48a,rgba(200,180,138,0) 75%),radial-gradient(ellipse 130px 160px at 150px 200px,#5a6a8a,rgba(90,106,138,0) 75%),radial-gradient(ellipse 320px 80px at 300px 400px,#2a2a22,rgba(0,0,0,0) 75%),linear-gradient(135deg,#5e6656,#8a8670 50%,#4a4a3c)" role="img" aria-label="Smiling home brewer bottling beer at a wooden table outdoors"></div>
<div class="abs welcome-bg"></div>
<div class="abs welcome-h">Welcome to <span>Maltkisten.dk</span></div>
<p class="abs welcome-p">Aliquam molestie, mi et imperdiet euismod, dui purus auctor tellus, et interdum lacus lectus et ante. Sed accumsan sollicitudin sapien, sit amet adipiscing turpis gravida ac. In congue, neque ac lobortis volutpat, libero mauris varius mi, vitae suscipit ipsum ligula vitae risus. Duis aliquam nibh a dui iaculis viverra id a velit. Vivamus egestas risus in magna varius commodo.</p>
<div class="abs btn" style="left:614px;top:1739px;width:152px;height:54px;line-height:54px">Read More</div>

<div class="section-title" style="top:1908px">Featured Products</div>
<svg class="arrow" style="left:47px;top:2160px" width="12" height="26" viewBox="0 0 12 26"><path d="M10 2 2 13l8 11" fill="none" stroke="#333" stroke-width="2"/></svg>
<svg class="arrow" style="left:1140px;top:2160px" width="12" height="26" viewBox="0 0 12 26"><path d="M2 2l8 11-8 11" fill="none" stroke="#333" stroke-width="2"/></svg>
<div class="prod" style="left:76px;top:1997px"><div class="img" style="background:radial-gradient(ellipse 70px 95px at 100px 110px,#b09670,#d8c8a8 55%,rgba(255,255,255,0) 80%)" role="img" aria-label="Bag of crushed malt with test kit"></div><h4>PRODUCT NAME</h4><p>Aliquam molestie</p><s>$79.00</s><b>$55.00</b></div>
<div class="prod" style="left:346px;top:1997px"><div class="img" style="background:radial-gradient(ellipse 22px 100px at 100px 110px,#c8a888,#e6d8c8 55%,rgba(255,255,255,0) 85%)" role="img" aria-label="Long bottle brush"></div><h4>PRODUCT NAME</h4><p>Aliquam molestie</p><s>$79.00</s><b>$55.00</b></div>
<div class="prod" style="left:615px;top:1997px"><div class="img" style="background:radial-gradient(ellipse 55px 100px at 100px 120px,#2e2e2e,#6a6a6a 50%,rgba(255,255,255,0) 82%)" role="img" aria-label="Bench bottle capper"></div><h4>PRODUCT NAME</h4><p>Aliquam molestie</p><s>$79.00</s><b>$55.00</b></div>
<div class="prod" style="left:886px;top:1997px"><div class="img" style="background:radial-gradient(ellipse 45px 100px at 100px 120px,#4a1a0a,#7a3418 55%,rgba(255,255,255,0) 82%)" role="img" aria-label="Amber glass bottle with cork"></div><h4>PRODUCT NAME</h4><p>Aliquam molestie</p><s>$79.00</s><b>$55.00</b></div>

<div class="abs brands"></div>
<div class="section-title" style="top:2472px">Shop Partner Brands</div>
<div class="badge" style="left:78px;top:2550px;width:138px;height:54px;border-radius:12px"></div>
<div class="badge" style="left:258px;top:2562px;width:32px;height:32px;border-width:3px;border-color:#666"></div>
<div class="badge" style="left:440px;top:2548px;width:56px;height:56px;border-radius:50%;background:#3a3a3a;border-color:#111"></div>
<div class="badge" style="left:556px;top:2548px;width:58px;height:58px;border-radius:50%;border-width:3px"></div>
<div class="badge" style="left:664px;top:2562px;width:126px;height:28px;background:var(--badge)"></div>
<div class="badge" style="left:846px;top:2558px;width:114px;height:38px;background:var(--badge)"></div>
<div class="badge" style="left:1046px;top:2542px;width:70px;height:70px;border-radius:50%;background:var(--badge)"></div>

<div class="tile" style="left:75px;top:2731px;width:512px;height:333px;background:radial-gradient(ellipse 200px 110px at 260px 280px,#b07a44,rgba(176,122,68,0) 75%),radial-gradient(ellipse 140px 100px at 320px 60px,#6a4a36,rgba(0,0,0,0) 75%),linear-gradient(135deg,#1e1a18,#3e3028 55%,#2a2220);font-size:38px;font-weight:700;line-height:44px" role="img" aria-label="Hands pouring malt grain into a brewing bag">Neque porro quisquam<br>est qui dolorem</div>
<div class="tile" style="left:615px;top:2731px;width:512px;height:333px;background:radial-gradient(ellipse 190px 150px at 260px 180px,#8a7450,rgba(138,116,80,0) 75%),radial-gradient(ellipse 230px 100px at 256px 60px,#5a6a3a,rgba(0,0,0,0) 75%),linear-gradient(135deg,#2e3a1e,#4a4a30 55%,#34401e);font-size:38px;font-weight:700;line-height:44px" role="img" aria-label="Foaming wort boiling in a steel kettle with a thermometer on the lawn">Neque porro quisquam<br>est qui dolorem</div>

<div class="abs mail"></div>
<div class="abs mail-h">Join our Mailing List</div>
<div class="abs mail-in">Enter Email Address</div>
<div class="abs mail-go"><svg style="margin:12px 18px" width="12" height="16" viewBox="0 0 12 16"><path d="M2 2l7 6-7 6" fill="none" stroke="#fff" stroke-width="2.5"/></svg></div>

<div class="section-title" style="top:3311px">Testimonials</div>
<p class="abs quote">" Aliquam molestie, mi et imperdiet euismod, dui purus auctor tellus, et interdum lacus lectus et ante sed accumsan sollicitudin sapien, sit amet adipiscing turpis gravida ac..."</p>
<div class="abs quote-by">-Name Heading</div>
<svg class="arrow" style="left:75px;top:3413px" width="10" height="20" viewBox="0 0 10 20"><path d="M8 2 2 10l6 8" fill="none" stroke="#555" stroke-width="2"/></svg>
<svg class="arrow" style="left:1115px;top:3413px" width="10" height="20" viewBox="0 0 10 20"><path d="M2 2l6 8-6 8" fill="none" stroke="#555" stroke-width="2"/></svg>

<div class="abs blog"></div>
<div class="section-title" style="top:3600px">Blog Posts</div>
<div class="photo" style="left:75px;top:3672px;width:512px;height:275px;background:radial-gradient(ellipse 230px 120px at 300px 240px,#fafafa,#e8e8e8 55%,rgba(232,232,232,0) 85%),radial-gradient(ellipse 160px 120px at 100px 80px,#1e1e1e,rgba(30,30,30,0) 80%),linear-gradient(135deg,#2a2a2a,#8a8a8a 50%,#d8d8d8)" role="img" aria-label="Pouring milky liquid into a white fermenting bucket"></div>
<div class="photo" style="left:615px;top:3672px;width:512px;height:275px;background:radial-gradient(ellipse 110px 80px at 250px 130px,#6a7a3a,#9a9a80 55%,rgba(0,0,0,0) 85%),radial-gradient(ellipse 140px 100px at 200px 220px,#c89a80,rgba(0,0,0,0) 75%),linear-gradient(135deg,#2a2622,#4a463c 50%,#8a8070)" role="img" aria-label="Hand holding a tub of green hop pellets"></div>
<div class="abs blog-date" style="left:75px;top:3972px">jun 29, 2020</div>
<div class="abs blog-title" style="left:75px;top:4000px">Vestibulum vel metus sit amet turpis bibendum tincidunt vel sit</div>
<div class="abs blog-date" style="left:615px;top:3972px">jun 29, 2020</div>
<div class="abs blog-title" style="left:615px;top:4000px">Vestibulum vel metus sit amet turpis bibendum tincidunt vel sit</div>

<div class="feature" style="left:75px">
  <svg width="36" height="34" viewBox="0 0 36 34"><rect x="2" y="14" width="7" height="18" fill="#333"/><path d="M12 14l8-12c3 0 4 2 3 5l-2 6h10c3 0 4 3 3 5l-3 11c-1 2-2 3-4 3H12z" fill="#333"/></svg>
  <h5>QUALITY PRODUCTS</h5><p>Suspendisse potenti</p>
</div>
<div class="feature" style="left:436px">
  <svg width="40" height="32" viewBox="0 0 40 32"><ellipse cx="16" cy="12" rx="15" ry="10" fill="#333"/><ellipse cx="26" cy="20" rx="13" ry="9" fill="#333"/><path d="M6 20l-3 8 9-5z" fill="#333"/></svg>
  <h5>CUSTOMER CARE</h5><p>Suspendisse potenti</p>
</div>
<div class="feature" style="left:797px">
  <svg width="34" height="34" viewBox="0 0 34 34"><path d="M4 30 18 16" stroke="#333" stroke-width="6" stroke-linecap="round"/><circle cx="24" cy="10" r="8" fill="#333"/><circle cx="28" cy="6" r="4" fill="#fff"/></svg>
  <h5>PERSONAL SERVICE</h5><p>Suspendisse potenti</p>
</div>

<div class="abs footer"></div>
<div class="fcol" style="left:75px"><h6>INFORMATION</h6>Information<br>About us<br>This is how you act<br>Secure trade<br>Instructions</div>
<div class="fcol" style="left:343px"><h6>CUSTOMER SERVICE</h6>Frequently asked questions<br>trading Terms<br>Privacy Policy<br>Here you find us<br>Contact us</div>
<div class="fcol contact" style="left:615px"><h6>CONTACT</h6>Malt Depot<br>Humlevej 14 8800 Viborg<br>CVR DK12345678<br>40 11 22 33<br>info@maltkisten.dk</div>
<div class="fcol" style="left:888px"><h6>SOCIAL NETWORKS</h6></div>
<div class="social" style="left:888px"></div>
<div class="social" style="left:928px"></div>
<div class="social" style="left:974px"></div>
<div class="social" style="left:1020px"></div>
<div class="abs fline"></div>
<div class="abs copy">Copyright © 2020. Company Name. All Right Reserved</div>
<div class="card" style="left:792px"></div>
<div class="card" style="left:850px"></div>
<div class="card" style="left:908px"></div>
<div class="card" style="left:966px"></div>
<div class="card" style="left:1024px"></div>
<div class="card" style="left:1082px"></div>

</body>
</html>
```